Business Card Design

We need a business card designed for a new company based in Melbourne called KPo solutions. KPo solutions provides management consulting specialising in the health and social services sector.

KPo solutions offer a unique set of specialist skills │dealing with all levels of government │ unique communication skills│intimate knowledge of the health sector │solutions tailored to unique circumstances.

KPo solutions takes on a select number of clients at any one time, this ensures that your organisation receives the attention required. On larger projects, KPo solutions join up with other consultants to bring specialist skills to a project.
Updates

This is the first time I have used Pattern Hive and thank you all for responding. The variation is amazing and makes it hard to decide. I have to ask some of my friends to give me their views. The response is fantastic. The one I pick will basically be the most visually appealing

Industry/Entity Type

Management Consulting

Contact Information for Business Card

Martin Hollis, Principal, KPo solutions, 14 Calloway Ave, Westbridge VIC 3094, 0438 712 304, martinh@kposolutions.com.au, www.kposolutions.com.au

```html
<!DOCTYPE html>
<html lang="en">
<head>
<meta charset="utf-8">
<title>KPo solutions — Business Card</title>
<link rel="stylesheet" href="https://fonts.googleapis.com/css2?family=Kelly+Slab&display=swap">
<style>
  :root {
    --brand-red: #bd202e;
    --brand-red-dark: #4a1519;
    --pattern-tint: #c9464f;
    --column-tint: #a61d29;
    --ink: #1a1a1a;
    --paper: #ffffff;
  }
  * { margin: 0; padding: 0; box-sizing: border-box; }
  html, body { width: 1200px; height: 741px; overflow: hidden; background: var(--paper); }
  .card {
    position: relative;
    width: 1200px;
    height: 741px;
    background: var(--paper);
    font-family: "Kelly Slab", Georgia, serif;
    font-weight: 400;
    color: var(--ink);
    overflow: hidden;
  }
  .banner {
    position: absolute;
    left: 0; top: 82px;
    width: 1200px; height: 224px;
    background: var(--brand-red);
  }
  .banner__pattern {
    position: absolute;
    left: 116px; top: 15px;
    width: 230px; height: 195px;
    background: var(--pattern-tint);
    opacity: 0.55;
  }
  .banner__column {
    position: absolute;
    left: 828px; top: 4px;
    width: 33px; height: 217px;
    background: var(--column-tint);
  }
  .brand-name {
    position: absolute;
    left: 400px; top: 0;
    width: 410px; height: 224px;
    display: flex;
    align-items: center;
    justify-content: center;
    color: var(--paper);
    font-size: 46px;
    line-height: 1;
    letter-spacing: 1px;
  }
  .person {
    position: absolute;
    left: 57px; top: 330px;
  }
  .person__name {
    font-size: 35px;
    font-weight: 400;
    color: var(--brand-red);
    line-height: 1.15;
    letter-spacing: 0.5px;
  }
  .person__role {
    font-size: 29px;
    line-height: 1.3;
  }
  .icon-tab {
    position: absolute;
    left: 0; top: 505px;
  }
  .contact {
    position: absolute;
    left: 60px; top: 507px;
    list-style: none;
    font-size: 23px;
    line-height: 31.5px;
    letter-spacing: 0.3px;
  }
  .contact li { white-space: nowrap; }
  .footer-bands { position: absolute; left: 0; top: 703px; }
</style>
</head>
<body>
<div class="card">
  <header class="banner">
    <div class="banner__pattern" role="img" aria-label="Decorative grid of small plus signs"></div>
    <div class="banner__column" role="img" aria-label="Decorative column of large plus signs"></div>
    <div class="brand-name">KPo solutions</div>
  </header>

  <section class="person">
    <h1 class="person__name">Martin Hollis</h1>
    <p class="person__role">Principal</p>
  </section>

  <svg class="icon-tab" width="46" height="142" viewBox="0 0 46 142" aria-hidden="true">
    <path d="M0 0 H38 a8 8 0 0 1 8 8 V134 a8 8 0 0 1 -8 8 H0 Z" fill="var(--brand-red)"/>
    <path d="M21 10 c-3 1 -4 4 -3 8 c1 4 4 8 7 10 c2 1 4 0 5 -2 l-3 -3 c-1 1 -2 1 -3 0 c-1 -2 -2 -4 -2 -6 c0 -1 1 -2 2 -2 l-1 -4 Z" fill="#fff"/>
    <rect x="13" y="45" width="26" height="17" fill="none" stroke="#fff" stroke-width="2"/>
    <path d="M13 45 L26 55 L39 45 M13 62 L23 53 M39 62 L29 53" fill="none" stroke="#fff" stroke-width="1.6"/>
    <circle cx="26" cy="84" r="11" fill="#fff"/>
    <path d="M20 78 c3 1 4 3 3 5 c-2 1 -1 4 1 5 l-1 4 c-3 -1 -5 -4 -5 -8 Z M29 76 c2 2 5 4 4 8 c-2 0 -3 2 -3 4 c-2 -2 -3 -5 -1 -7 Z" fill="var(--brand-red)"/>
    <path d="M26 106 a8 8 0 0 1 8 8 c0 6 -8 15 -8 15 c0 0 -8 -9 -8 -15 a8 8 0 0 1 8 -8 Z" fill="#fff"/>
    <circle cx="26" cy="114" r="3" fill="var(--brand-red)"/>
  </svg>

  <ul class="contact">
    <li class="contact__phone">438 712 304</li>
    <li class="contact__email">martinh@kposolutions.com.au</li>
    <li class="contact__web">www.kposolutions.com.au</li>
    <li class="contact__address">KPo solutions</li>
    <li class="contact__address">14 Calloway Ave</li>
    <li class="contact__address">Westbridge VIC 3094</li>
  </ul>

  <svg class="footer-bands" width="1200" height="38" viewBox="0 0 1200 38" aria-hidden="true">
    <polygon points="0,0 392,0 409,38 0,38" fill="var(--brand-red)"/>
    <polygon points="399,6 1200,6 1200,15 403,15" fill="var(--brand-red)"/>
    <polygon points="405,18 1200,18 1200,38 414,38" fill="var(--brand-red-dark)"/>
  </svg>
</div>
</body>
</html>
```